pelmora.com

Design proposals for a gold bank site and gold wallet main page. The site will let people (and companies) open accounts and purchase gold for deposit and later make payments with the gold they hold in the bank. The bank will be a e-money licensed venture located in Switzerland. The functionality of the "system" will be very simple and possibly only use icon symbols so it can be multilingual.

The mainstays of the site will be security and trust. Al digital gold is backed 100 % by visible gold in vault audited every day.

Target Market(s)

Asian and American gold buyers and people preferring gold to currency

Industry/Entity Type

Security

Requirements
Must have
• a) Logo
b) Main index page with a new logo and design
c) System (post log in e-wallet) main page showing the last transactions of the client and give client options to transfer funds and make deposits
Nice to have
• sample contact form
sample faq page
terms page design
Should not have
• So much text since it will be aimed at the worldwide market

```html
<!DOCTYPE html>
<html lang="en">
<head>
<meta charset="utf-8">
<title>pelmora — gold bank</title>
<link href="https://fonts.googleapis.com/css2?family=PT+Sans:wght@400;700&family=PT+Sans+Narrow:wght@400;700&display=swap" rel="stylesheet">
<style>
:root{
  --gold:#e3b23c;
  --gold-dark:#c48d22;
  --gold-text:#f0c419;
  --link-gold:#a5781a;
  --ink:#222;
  --text:#3a3a3a;
  --muted:#777;
  --paper:#efede6;
  --panel-top:#ffffff;
  --panel-bottom:#e6e6e6;
  --line:#cfcfcf;
  --cream:#fbf6cf;
  --black-top:#3a3a3a;
  --black-bottom:#0b0b0b;
}
*{margin:0;padding:0;box-sizing:border-box}
html,body{width:1200px;height:744px;overflow:hidden}
body{position:relative;background:var(--paper);font-family:"PT Sans",sans-serif;color:var(--text)}
.abs{position:absolute}

/* header */
.header-band{left:0;top:0;width:1200px;height:142px;background:linear-gradient(#f0c65a,#d8a536 70%,#c99527)}
.header-panel{left:108px;top:-2px;width:983px;height:100px;border-radius:0 0 10px 10px;background:linear-gradient(var(--panel-top),var(--panel-bottom));border:1px solid #d4b25e;box-shadow:0 2px 3px rgba(0,0,0,.2)}
.brand{left:131px;top:16px;display:flex;align-items:center;gap:14px}
.brand-mark{width:62px;height:62px;border-radius:50%;background:var(--gold)}
.brand-name{font-size:44px;font-weight:700;color:var(--ink);letter-spacing:-.5px}
.search{left:685px;top:60px;width:160px;height:23px;display:flex}
.search-field{flex:1;border:1px solid #b9b9b9;border-right:0;border-radius:4px 0 0 4px;background:#fff;font-size:11px;color:#9aa;padding:4px 6px}
.search-btn{width:35px;background:linear-gradient(#f2c540,#d09a1c);border-radius:0 4px 4px 0;display:flex;align-items:center;justify-content:center}
.util-nav{left:845px;top:62px;display:flex;font-size:12px;color:var(--ink)}
.util-nav span{padding:0 10px;border-left:1px solid #ccc;line-height:18px}
.util-nav span:first-child{border-left:0}
.main-nav{left:108px;top:110px;display:flex;font-size:14px;color:#fff}
.main-nav span{padding:0 11px;border-left:1px solid #a9791c;line-height:22px}
.main-nav span:first-child{border-left:0;color:var(--ink);font-weight:700;padding-left:7px}
.login{left:998px;top:106px;width:69px;height:28px;background:var(--cream);border-radius:4px;font-size:14px;color:var(--ink);text-align:center;line-height:28px}

/* contact */
.phone{font-size:14px;color:#555}
.phone b{color:#444}
.phone small{font-size:10px}
.phone-note{font-size:10px;color:#555}
.hours{left:966px;top:172px;font-size:10px;color:#444;border-bottom:1px dotted #666;padding-bottom:2px}

/* hero */
.hero{left:110px;top:209px;width:674px;height:280px;border:1px solid #d6d2c2;border-radius:8px;overflow:hidden;background:linear-gradient(90deg,#f7f2e2 0%,#f4ecd2 40%,#e9cf7e 60%,#d9b24a 100%)}
.hero-photo{position:absolute;left:270px;top:0;width:404px;height:280px;background:radial-gradient(circle at 35% 55%,#e9b92a 0%,#c98c14 25%,rgba(201,140,20,0) 50%),linear-gradient(120deg,rgba(240,225,180,0),#c7b3d8 55%,#d6c6a6 75%,#a992c2 100%)}
.hero h1{position:absolute;left:19px;top:66px;font-family:"PT Sans Narrow",sans-serif;font-size:33px;color:#111;letter-spacing:-1px}
.hero p{position:absolute;left:19px;top:109px;width:268px;font-size:11px;line-height:16px;color:#333}

.promo{left:795px;top:209px;width:295px;height:138px;border:1px solid #c9c9c9;border-radius:8px;background:linear-gradient(#fafafa,#e4e4e4)}
.promo-title{position:absolute;left:9px;top:7px;font-size:16px;color:#333;line-height:19px}
.promo-title b{display:block}
.promo-sub{position:absolute;left:10px;top:49px;font-size:11px;color:#888}
.promo-art{position:absolute;left:170px;top:24px;width:116px;height:92px;background:radial-gradient(ellipse at 50% 55%,#f1c232,#c98f10 60%,rgba(0,0,0,0) 75%)}
.btn-dark{position:absolute;left:14px;top:95px;width:83px;height:30px;border-radius:4px;background:linear-gradient(#4a4a4a,#1e1e1e);border:1px solid #111;color:#f4f0cc;font-size:12px;text-align:center;line-height:28px}

.offer{left:795px;top:351px;width:295px;height:137px;border-radius:8px;background:radial-gradient(ellipse at 80% 40%,var(--black-top),var(--black-bottom) 70%)}
.offer-title{position:absolute;left:15px;top:5px;font-size:31px;font-weight:700;color:#fff}
.offer-sub{position:absolute;left:15px;top:39px;font-size:18px;font-weight:700;color:var(--gold-text)}
.offer-note{position:absolute;left:16px;top:63px;font-size:11px;line-height:14px;color:#c9c9c9}
.btn-cream{position:absolute;left:15px;top:99px;width:82px;height:28px;border-radius:4px;background:var(--cream);color:#222;font-size:12px;text-align:center;line-height:28px}

/* feature cards */
.card{top:511px;height:149px;border:1px solid #c4c4c4;border-radius:6px;overflow:hidden;background:linear-gradient(#fff,#dedede)}
.card h2{height:38px;background:linear-gradient(var(--black-top),var(--black-bottom));color:#fff;font-size:19px;font-weight:400;padding:8px 13px 0}
.card p{position:absolute;left:12px;top:46px;font-size:11px;line-height:16px;color:#333}
.card .more{position:absolute;right:9px;bottom:4px;font-size:11px;color:var(--link-gold)}
.card-art{position:absolute;left:193px;top:49px;width:95px;height:60px;border-radius:4px;background:linear-gradient(135deg,#f3dcae,#c98b3f 60%,#8a5a22)}

/* footer */
.footer{left:0;top:686px;width:1200px;height:58px;background:linear-gradient(#fff,#e0e0e0);border-top:1px solid #ccc}
.foot-brand{left:121px;top:697px;display:flex;align-items:center;gap:10px}
.foot-mark{width:30px;height:30px;background:#9a9a9a;border-radius:50%}
.foot-name{font-size:25px;font-weight:700;color:#2a2a2a}
.foot-links{left:395px;top:704px;font-size:11px;color:#777;word-spacing:2px}
.foot-links i{font-style:normal;margin:0 13px}
.copyright{left:547px;top:723px;font-size:10px;color:#777}
.follow{left:935px;top:708px;font-size:12px;color:#555}
.social{left:995px;top:707px;display:flex;gap:3px}
.social span{width:16px;height:16px;border-radius:2px}
</style>
</head>
<body>

<div class="abs header-band"></div>
<div class="abs header-panel"></div>
<div class="abs brand"><span class="brand-mark"></span><span class="brand-name">pelmora</span></div>

<div class="abs search">
  <div class="search-field">search</div>
  <div class="search-btn">
    <svg width="16" height="16" viewBox="0 0 16 16"><circle cx="6.5" cy="6.5" r="4.5" fill="none" stroke="#fff" stroke-width="2"/><line x1="10" y1="10" x2="14" y2="14" stroke="#fff" stroke-width="2.5" stroke-linecap="round"/></svg>
  </div>
</div>
<nav class="abs util-nav">
  <span>global</span><span>contact us</span><span>help</span>
  <span>security <svg width="9" height="11" viewBox="0 0 9 11"><path d="M2 5V3.5a2.5 2.5 0 0 1 5 0V5" fill="none" stroke="#b49a22" stroke-width="1.4"/><rect x="0.5" y="5" width="8" height="6" rx="1" fill="#b49a22"/></svg></span>
</nav>

<nav class="abs main-nav">
  <span>Home</span><span>How to order</span><span>Buy Gold</span><span>Buy Silver</span><span>About us</span><span>FAQ</span><span>Open an Account</span>
</nav>
<div class="abs login">Log in</div>

<div class="abs phone" style="left:688px;top:151px"><b>Bank:</b> 0-123-456-789 <small>(2559)</small></div>
<div class="abs phone-note" style="left:688px;top:173px">call us 24/7 | &nbsp;call wait time: 0 min</div>
<div class="abs phone" style="left:896px;top:151px"><b>Auto:</b> 0-123-456-789 <small>(2559)</small></div>
<div class="abs hours">Hours of Operation</div>

<section class="abs hero">
  <div class="hero-photo" role="img" aria-label="Gold bar and gold nuggets resting on euro banknotes over a rising price chart"></div>
  <h1>GOLD COINS</h1>
  <p>Lorem Ipsum is simply dummy text of the printing and typesetting industry. Lorem Ipsum has been the industry's standard dummy text ever since the 1500s, when an unknown printer took a galley of type and scrambled it to make a type specimen book.</p>
</section>

<section class="abs promo">
  <div class="promo-title">Make a<b>Payment On your Gold</b></div>
  <div class="promo-sub">Enroll &nbsp;&nbsp;learn more at pelmora</div>
  <div class="promo-art" role="img" aria-label="Stacked gold bars"></div>
  <div class="btn-dark">Read More</div>
</section>

<section class="abs offer">
  <div class="offer-title">BUY GOLD</div>
  <div class="offer-sub">ON ORDERS OVER $</div>
  <div class="offer-note">THIS OFFER IS VALID ON ALL<br>OUR &nbsp;STORE ITEMS</div>
  <div class="btn-cream">Read More</div>
</section>

<section class="abs card" style="left:111px;width:304px">
  <h2>Sell Us Gold</h2>
  <p>Lorem Ipsum is simply dummy text of the printing<br>and typesetting industry. Lorem Ipsum has been the<br>industry's standard dummy text ever since the 1500s,<br>when an unknown printer took a galley of type and<br>scrambled it to make a type specimen book.</p>
  <span class="more">Learn &nbsp;more ››</span>
</section>

<section class="abs card" style="left:453px;width:303px">
  <h2>Buy Silver Coins</h2>
  <p>Lorem Ipsum is simply dummy text of the printing<br>and typesetting industry. Lorem Ipsum has been the<br>industry's standard dummy text ever since the 1500s,<br>when an unknown printer took a galley of type and<br>scrambled it to make a type specimen book.</p>
  <span class="more">Learn &nbsp;more ››</span>
</section>

<section class="abs card" style="left:788px;width:303px">
  <h2>E-Walltet</h2>
  <p>Lorem Ipsum is simply dummy<br>text of the printing and typeset-<br>ting industry.</p>
  <div class="card-art" role="img" aria-label="Gold wallet payment card"></div>
  <span class="more">Get Started &nbsp;››</span>
</section>

<footer class="abs footer"></footer>
<div class="abs foot-brand"><span class="foot-mark"></span><span class="foot-name">pelmora</span></div>
<div class="abs foot-links">Careers<i>|</i>Privacy<i>|</i>Security<i>|</i>Legal<i>|</i>Site map<i>|</i>give feedback</div>
<div class="abs copyright">© 2011-2012 pelmora.com</div>
<div class="abs follow">follow us</div>
<div class="abs social">
  <span style="background:#3aa7d9"></span>
  <span style="background:#3b5b9a"></span>
  <span style="background:#d1412f"></span>
  <span style="background:#c4302b"></span>
  <span style="background:#f08a24"></span>
</div>

</body>
</html>
```